Stationary for Velmo HPG, LLC
Company Name and slogan: Name: Velmo HPG, LLC and slogan "(removed from lockup)"
Stationary for Velmo HPG, LLC - Real Estate
Creative Brief
Use specific fonts
You can use the logo fonts or any fonts you deem creatively important.
Professional
Curtis Pellow
Solutions Specialist
41 Quarrington Court, Box 352 Dunmore Ridge, NJ 07381
cpellow@velmohpg-example.com
http://www.velmohpg-example.com
The Logo can be moved to the side of the company name and slogan if needed. The 3 items below do not have to be on the front of the business card if it will take from the design. *1 is most important of the 3. *1. We Buy Houses, Help with Foreclosures, CALL NOW!!! 2. We provide real estate solutions 3. Working together to make a difference. Also on back of business cards the * is a bullet or whatever you think is needed.
Company Name and slogan: Name: Velmo HPG, LLC and slogan "(removed from lockup)" Benefits: * We give immediate debt relief * We stop foreclosure * We pay down your mortgage * We increase your equity * We save you marketing $$ * We will sell your house for you * We save you on Realtors commissions * We find you a buyer * We allow you to keep your tax breaks CALL NOW!!! 201-555-0186

```html
<!DOCTYPE html>
<html lang="en">
<head>
<meta charset="utf-8">
<title>Velmo HPG, LLC – Business Card</title>
<link href="https://fonts.googleapis.com/css2?family=Arimo:wght@400;700&display=swap" rel="stylesheet">
<style>
  :root{
    --backdrop:#e8e5e1;
    --card-white:#ffffff;
    --brand-purple:#8e2b8c;
    --contact-blue:#2a78b0;
    --white:#ffffff;
  }
  *{margin:0;padding:0;box-sizing:border-box}
  html,body{width:1200px;height:751px;overflow:hidden}
  body{background:var(--backdrop);font-family:"Arimo",Arial,sans-serif;position:relative}
  .card{position:absolute;left:355px;width:490px;height:285px;box-shadow:0 2px 6px rgba(0,0,0,.25)}
  .card-front{top:55px;background:var(--card-white)}
  .card-back{top:365px;background:var(--brand-purple);color:var(--white)}

  .name-band{position:absolute;left:276px;top:24px;width:214px;height:60px;background:var(--brand-purple);color:var(--white);padding:10px 0 0 12px}
  .person-name{font-weight:700;font-size:17px;line-height:20px}
  .person-title{font-size:13px;line-height:20px;margin-top:2px}

  .brand{position:absolute;display:flex;align-items:center;gap:8px;justify-content:center}
  .brand-front{left:20px;top:180px;width:230px;color:var(--brand-purple)}
  .brand-mark{flex:none;width:16px;height:16px;border-radius:50%;background:currentColor}
  .brand-name{font-weight:700;font-size:22px;line-height:26px;white-space:nowrap}

  .contact{position:absolute;left:298px;top:150px;color:var(--contact-blue);font-size:12.5px;line-height:15px;font-style:normal}
  .contact .gap{height:8px}

  .benefits{position:absolute;left:22px;top:14px}
  .benefits-title{font-weight:700;font-size:15px;line-height:20px;margin-bottom:4px}
  .benefits-list{list-style:none}
  .benefits-list li{font-size:12.5px;line-height:15.6px;padding-left:14px;position:relative}
  .benefits-list li::before{content:"";position:absolute;left:2px;top:6px;width:5px;height:5px;border-radius:50%;background:var(--white)}

  .brand-back{left:280px;top:118px;width:200px;color:var(--white)}
  .brand-back .brand-name{font-size:20px;line-height:24px}
  .brand-back .brand-mark{width:14px;height:14px}

  .call-box{position:absolute;left:280px;top:220px;width:210px;height:55px;background:var(--white);color:var(--brand-purple);font-weight:700;padding:6px 0 0 14px}
  .call-label{font-size:19px;line-height:22px}
  .call-number{font-size:22px;line-height:24px}
</style>
</head>
<body>
  <section class="card card-front">
    <div class="name-band">
      <p class="person-name">Curtis Pellow</p>
      <p class="person-title">Solutions Specialist</p>
    </div>
    <div class="brand brand-front">
      <span class="brand-mark"></span>
      <p class="brand-name">Velmo HPG, LLC</p>
    </div>
    <address class="contact">
      <p>41 Quarrington Court, Box 352</p>
      <p>Dunmore Ridge, NJ 07381</p>
      <div class="gap"></div>
      <p>T&nbsp;&nbsp;: 201 555 0186</p>
      <p>F&nbsp;&nbsp;: 201 555 0186</p>
      <p>M : 201 555 0143</p>
      <p>cpellow@velmohpg-example.com</p>
      <p>www.velmohpg-example.com</p>
    </address>
  </section>

  <section class="card card-back">
    <div class="benefits">
      <p class="benefits-title">Benefits:</p>
      <ul class="benefits-list">
        <li>We Buy Houses, Help with Foreclosures</li>
        <li>We provide real estate solutions</li>
        <li>Working together to make a difference</li>
        <li>We give immediate debt relief</li>
        <li>We stop foreclosure</li>
        <li>We pay down your mortgage</li>
        <li>We increase your equity</li>
        <li>We save you marketing $$</li>
        <li>We will sell your house for you</li>
        <li>We save you on Realtors commissions</li>
        <li>We find you a buyer</li>
        <li>We allow you to keep your tax breaks</li>
      </ul>
    </div>
    <div class="brand brand-back">
      <span class="brand-mark"></span>
      <p class="brand-name">Velmo HPG, LLC</p>
    </div>
    <div class="call-box">
      <p class="call-label">CALL NOW!!!</p>
      <p class="call-number">201 555 0186</p>
    </div>
  </section>
</body>
</html>
```